Webdesign für Schweizer Online Drogerie Discounter
Zielgruppe
pflegolix.ch ist seit august 2017 der erste online drogerie discounter in der schweiz. mit 35’000 artikeln decken wir das aktuell verfügbare online sortiment an drogerieartikeln in der schweiz zu unschlagbar günstigen preisen ab.
dank dauertiefpreisen kaufen benutzer vor allem wegen der günstigen konditionen und des guten services bei pflegolix ein. alle artikel werden in der regel innert 24 h ab schweizer lager mit der rovena kurier versandt.
die kundenvorteile von pflegolix auf einen blick:
- über 35'000 artikel
- markenprodukte
- versand innert 24 h (sonst versandzeit pro artikel auf shop angegeben)
- lieferung via rovena kurier priority
- alle produkte ab schweizer lager
- bestellung auf rechnung möglich
- monatsrechnung möglich
- teilzahlung möglich
- kundendienst auf schwyzerdütsch
- neutrale, diskrete verpackung
- geld zurück garantie
Aufgabenstellung
- wir beschränken uns bewusst auf nur zwei seitentypen: homepage und produktdetailseite, weitere seiten sind optional. bei weiterführung des auftrages werden wir insbesondere auf checkout etc wert legen. kategorieübersicht ist optional
- wir suchen nicht nur ein neues design sondern inbesondere ein talent das uns weiter begleitet in screendesign, usability & user experience
- die vorschläge sollen nicht nur visuell überzeugen sondern auch funktional und in bezug auf user experience
- wir suchen auch nach dem vorschlag mit der besten user experience
- wir möchten auch elemente sehen bzgl benutzerführung
- wir planen die zusammenarbeit mit dem gewinner fortuzuführen und tiefer in den checkout prozess und weitere seiten einzutauchen
- wir müssen das design auf magento umsetzen
- es sollen weitere shops mit anderem logo und anderer grundfarbe ebenfalls auf dem design aufsetzen können oder weitere änderungen
- WICHTIG: wir suchen (natürlich) ein redesign und einen relaunch von pflegolix sowie eine multiplizierbare vorlage für unseren magento multishop auf welcher wir mehre shops abbilden können, aber wir suchen vor allem auch ein talent in screendesign und user experience das uns die nächste zeit beim aufbau unserer aktivitäten begleitet

```html
<!DOCTYPE html>
<html lang="de">
<head>
<meta charset="utf-8">
<title>pflegolix.ch – Produktdetail</title>
<link href="https://fonts.googleapis.com/css2?family=Poppins:ital,wght@0,300;0,400;0,500;0,600;0,700;0,800;1,800&display=swap" rel="stylesheet">
<style>
:root{
  --red:#e30613;
  --ink:#111;
  --text:#555;
  --muted:#888;
  --line:#dcdcdc;
  --band:#e2e2e2;
  --panel:#f3f3f3;
  --row:#ebebeb;
  --green:#5aa51e;
  --pay:#444;
}
*{box-sizing:border-box;margin:0;padding:0}
html,body{width:1061px;height:1200px;overflow:hidden;background:#fff}
body{font-family:"Poppins",sans-serif;color:var(--ink);position:relative;font-size:8px}
.abs{position:absolute}
a{color:inherit;text-decoration:none}

/* header */
.brand{left:200px;top:20px;display:flex;align-items:center;gap:6px}
.brand-dot{width:24px;height:24px;border-radius:50%;background:var(--red)}
.brand-name{font-size:22px;font-weight:700;color:var(--red);letter-spacing:-.5px}
.search{left:439px;top:25px;width:242px;height:22px;border:1px solid var(--line);display:flex}
.search span{flex:1;padding:4px 9px;font-size:9px;color:#999}
.search i{width:24px;border-left:1px solid var(--line);display:flex;align-items:center;justify-content:center}
.head-tools{left:717px;top:16px;height:42px;display:flex;border-left:1px solid var(--line)}
.tool{width:69px;border-right:1px solid var(--line);display:flex;flex-direction:column;align-items:center;justify-content:flex-end;font-size:6.5px;color:#777;letter-spacing:.3px;gap:4px;position:relative}
.badge{position:absolute;top:0;left:38px;width:11px;height:11px;border-radius:50%;background:var(--red);color:#fff;font-size:6px;display:flex;align-items:center;justify-content:center}

.nav{left:0;top:75px;width:1061px;height:28px;background:var(--band)}
.nav ul{position:absolute;left:200px;top:2px;display:flex;list-style:none;height:24px;align-items:center}
.nav li{font-size:8.6px;font-weight:600;padding:0 9.6px;letter-spacing:.2px;line-height:24px}
.nav li.active{background:#fff;color:var(--red);padding:0 9.5px}

.crumbs{left:201px;top:109px;font-size:7.5px;color:#666;display:flex;gap:6px;align-items:center}
.rule{height:1px;background:var(--line)}

/* product */
.product-img{left:236px;top:164px;width:94px;height:130px;background:linear-gradient(90deg,#7cab4a 0%,#c44 40%,#2a0f14 60%,#5b1020 100%);border-radius:4px}
.title{left:370px;top:148px;font-size:13.6px;font-weight:600}
.specs{left:371px;top:182px;width:345px}
.spec{display:flex;height:15.5px;align-items:center;font-size:7.6px}
.spec b{width:111px;font-weight:600}
.spec span{color:var(--text)}
.spec .more{color:var(--red);text-decoration:underline}
.nutri{left:477px;top:321px;width:239px}
.nutri div{display:flex;height:15.5px;align-items:center;font-size:7.6px;color:var(--text);padding-left:5px}
.nutri div:nth-child(odd){background:var(--row)}
.nutri em{font-style:normal;width:100px}
.nutri-label{left:371px;top:323px;font-size:7.6px;font-weight:600}

/* buy box */
.buy{left:733px;top:146px;width:127px;height:189px;background:var(--panel);border:1px solid #e4e4e4;padding:0 8px}
.price{font-size:32px;font-weight:800;font-style:italic;letter-spacing:-.5px;margin-top:4px;text-shadow:1px 1px 2px rgba(0,0,0,.25)}
.vat{font-size:6px;color:#555;margin-top:-2px;padding-bottom:8px;border-bottom:1px solid var(--line)}
.facts{margin-top:8px}
.fact{display:flex;align-items:center;height:14px;font-size:7.3px}
.fact svg{width:9px;margin-right:5px}
.fact b{width:45px;font-weight:600}
.fact span{color:#666}
.fact.ok b,.fact.ok span{color:var(--green)}
.qty{margin-top:10px;height:22px;border:1px solid var(--line);background:#fff;display:flex;font-size:9px}
.qty span{width:24px;display:flex;align-items:center;justify-content:center;color:#666}
.qty span.n{flex:1;border-left:1px solid var(--line);border-right:1px solid var(--line);color:#222;font-size:8px}
.cart-btn{margin-top:4px;height:21px;background:var(--red);color:#fff;font-size:8px;font-weight:700;display:flex;align-items:center;justify-content:center;gap:6px}

.rabatt{left:733px;top:353px;width:126px;height:174px;background:var(--panel);border:1px solid #e4e4e4;padding:7px 8px}
.rabatt h3{font-size:12.5px;font-weight:700}
.rabatt p{font-size:7.4px;font-weight:700;color:#555;line-height:1.25;margin-top:3px}
.tiers{margin-top:11px}
.tier{display:flex;justify-content:space-between;align-items:center;height:17.7px}
.tier i{font-style:normal;color:#fff;font-weight:700;font-size:11px;width:40px;height:15px;padding-left:3px;line-height:15px;clip-path:polygon(0 0,78% 0,100% 50%,78% 100%,0 100%)}
.tier span{font-size:12.5px;color:#333}

.usp{left:733px;top:546px;width:126px;height:264px;background:var(--panel);border:1px solid #e0e0e0}
.usp-cell{height:88px;border-bottom:1px solid #e0e0e0;display:flex;flex-direction:column;align-items:center;justify-content:flex-end;padding-bottom:14px;text-align:center;font-size:12.6px;line-height:1.2}
.usp-cell:last-child{border-bottom:0}
.usp-cell svg{margin-bottom:6px}
.usp-cell b{font-weight:700}

/* description */
.desc-h{left:201px;top:419px;font-size:10.6px;font-weight:700}
.desc{left:201px;top:443px;width:515px;font-size:7.7px;line-height:14px;color:var(--text)}

/* similar */
.sim-h{left:200px;top:612px;width:516px;text-align:center;font-size:20px;font-weight:700}
.sim-sub{left:200px;top:639px;width:516px;text-align:center;font-size:12px}
.card{top:677px;width:151px;height:168px;border:1px solid #d8d8d8}
.card .pic{position:absolute;left:40px;top:8px;width:72px;height:104px;border-radius:4px}
.card .p{position:absolute;right:10px;top:84px;font-size:28px;font-weight:800;font-style:italic;color:#111;text-shadow:0 0 3px #fff,0 0 3px #fff,1px 2px 3px rgba(0,0,0,.35)}
.card .name{position:absolute;left:11px;top:129px;font-size:10px;font-weight:700;line-height:1.2}

/* service */
.q-h{left:205px;top:885px;font-size:10.6px;font-weight:700;color:#555}
.contact{top:910px;display:flex;align-items:center;gap:9px;height:50px}
.contact b{display:block;color:var(--red);font-weight:500;font-size:14px;line-height:1.2}
.contact span{font-size:9px}
.vsep{top:910px;width:1px;height:48px;background:var(--line)}
.pay-h{left:207px;top:984px;font-size:10.6px;font-weight:700;color:#555}
.ship-h{left:781px;top:994px;font-size:10.6px;font-weight:700;color:#555}
.pay{top:1024px;width:77px;height:27px;display:flex;align-items:center;justify-content:center;font-size:8.5px;font-weight:600;color:var(--pay)}
.pay-sep{top:1026px;width:1px;height:23px;background:var(--line)}

/* footer */
.f-brand{left:205px;top:1090px;display:flex;align-items:center;gap:5px}
.f-brand i{width:18px;height:18px;border-radius:50%;background:#9a9a9a}
.f-brand span{font-size:16px;font-weight:600;color:#8a8a8a}
.f-h{top:1090px;font-size:10.3px;font-weight:700;color:#555}
.f-txt{font-size:7.8px;color:#444;line-height:11px}
.f-list{list-style:none;font-size:7.8px;color:#444;line-height:10.7px}
.f-list li::before{content:"›";margin-right:5px}
.news{left:713px;top:1154px;width:147px;height:22px;border:1px solid var(--line);display:flex}
.news span{flex:1;font-size:8.5px;color:#999;padding:4px 8px}
.news i{width:24px;background:#111;display:flex;align-items:center;justify-content:center}
</style>
</head>
<body>

<!-- header -->
<div class="abs brand"><i class="brand-dot"></i><span class="brand-name">pflegolix.ch</span></div>
<div class="abs search"><span>Suchbegriff eingeben</span><i><svg width="9" height="9" viewBox="0 0 10 10"><circle cx="4" cy="4" r="3" fill="none" stroke="#111" stroke-width="1.6"/><path d="M6.3 6.3 9 9" stroke="#111" stroke-width="1.8"/></svg></i></div>
<div class="abs head-tools">
  <div class="tool"><svg width="13" height="15" viewBox="0 0 13 15"><circle cx="6.5" cy="4" r="3.6" fill="#999"/><path d="M0 15c0-5 3-7 6.5-7S13 10 13 15z" fill="#999"/></svg>KUNDENKONTO</div>
  <div class="tool"><span class="badge">8</span><svg width="16" height="14" viewBox="0 0 16 14"><path d="M0 1h3l2 8h9l2-6H4" fill="none" stroke="#999" stroke-width="1.8"/><circle cx="6" cy="12" r="1.5" fill="#999"/><circle cx="13" cy="12" r="1.5" fill="#999"/></svg>WARENKORB</div>
</div>

<nav class="abs nav"><ul>
  <li class="active">NAHRUNG/NAHRUNGSERGÄNZER</li><li>KOSMETIK/KÖRPERPFLEGE</li><li>MEDIZIN</li><li>ALTERNATIVMEDIZIN</li><li>BABY</li><li>HAUSHALT</li><li>TIERARTIKEL</li>
</ul></nav>

<div class="abs crumbs"><svg width="8" height="7" viewBox="0 0 8 7"><path d="M0 3.5 4 0l4 3.5H7V7H5V5H3v2H1V3.5z" fill="var(--red)"/></svg>›<span>Kategoriename</span>›<span>Breadcrumb</span></div>
<div class="abs rule" style="left:200px;top:124px;width:660px"></div>

<!-- product -->
<div class="abs product-img" role="img" aria-label="Produktfoto: Faltschachtel und dunkle Glasflasche Bio-Fruchtsaft"></div>
<h1 class="abs title">Lorem ipsum dolor sit amet</h1>
<div class="abs specs">
  <div class="spec"><b>Menge / Grösse</b><span>100 Kapseln</span></div>
  <div class="spec"><b>Marke</b><span>Valnorin</span></div>
  <div class="spec"><b>Artikelnummer</b><span>512331241231</span></div>
  <div class="spec"><b>Kategorie</b><span>Öl</span></div>
  <div class="spec"><b>Hersteller / Vertrieb</b><span>Valnorin AG</span></div>
  <div class="spec"><b>Herkunft</b><span>Schweiz</span></div>
  <div class="spec"><b>Labels</b><span>XXX</span></div>
  <div class="spec"><b>Gütesiegel</b><span>XXX</span></div>
  <div class="spec"><b>Inhaltsstoffe</b><span>Lorem, Ipsum, Dolor, Sit, Amet... <a class="more">mehr...</a></span></div>
</div>
<div class="abs nutri-label">Nährwerte auf 100g/ml</div>
<div class="abs nutri">
  <div><em>Energie / Brennwert</em>33,5 kJ / 8 kcal</div>
  <div><em>Eiweiss / Proteine</em>0 g</div>
  <div><em>Kohlenhydrate</em>0 g</div>
  <div><em>Fett</em>0,9 g</div>
</div>
<div class="abs rule" style="left:200px;top:392px;width:516px"></div>

<!-- buy box -->
<aside class="abs buy">
  <div class="price">45.99</div>
  <div class="vat">inkl. Mehrwertsteuer</div>
  <div class="facts">
    <div class="fact ok"><svg viewBox="0 0 9 9"><rect x=".5" y="1.5" width="8" height="7" fill="none" stroke="#999"/><path d="M.5 3.5h8" stroke="#999"/></svg><b>Lieferzeit</b><span>2-3 Tage</span></div>
    <div class="fact"><svg viewBox="0 0 9 9"><rect x="0" y="2" width="6" height="4.5" fill="#888"/><path d="M6 3.5h2l1 1.5v1.5H6z" fill="#888"/><circle cx="2" cy="7.5" r="1" fill="#888"/><circle cx="7" cy="7.5" r="1" fill="#888"/></svg><b>Versand</b><span>CHF 3,90</span></div>
    <div class="fact"><svg viewBox="0 0 9 9"><path d="M4.5 .5 8.5 2.5v4l-4 2-4-2v-4z" fill="none" stroke="#888"/><path d="M.5 2.5l4 2 4-2M4.5 4.5v4" stroke="#888" fill="none"/></svg><b>Bestand</b><span>Auf Lager</span></div>
  </div>
  <div class="qty"><span>–</span><span class="n">1</span><span>+</span></div>
  <div class="cart-btn"><svg width="11" height="9" viewBox="0 0 16 14"><path d="M0 1h3l2 8h9l2-6H4" fill="none" stroke="#fff" stroke-width="2"/><circle cx="6" cy="12" r="1.6" fill="#fff"/><circle cx="13" cy="12" r="1.6" fill="#fff"/></svg>In den Warenkorb</div>
</aside>

<aside class="abs rabatt">
  <h3>Rabattsystem</h3>
  <p>Sie erhalten folgende Rabatte...</p>
  <div class="tiers">
    <div class="tier"><i style="background:#f47a7a">3%</i><span>ab 25.00</span></div>
    <div class="tier"><i style="background:#f26565">4%</i><span>ab 50.00</span></div>
    <div class="tier"><i style="background:#ef4c4c">5%</i><span>ab 100.00</span></div>
    <div class="tier"><i style="background:#ec3535">6%</i><span>ab 200.00</span></div>
    <div class="tier"><i style="background:#e81f1f">7%</i><span>ab 500.00</span></div>
    <div class="tier"><i style="background:var(--red)">10%</i><span>ab 750.00</span></div>
  </div>
</aside>

<aside class="abs usp">
  <div class="usp-cell"><svg width="24" height="19" viewBox="0 0 24 19"><rect x="0" y="2" width="15" height="12" rx="1" fill="#8d8d8d"/><path d="M15 6h5l4 4v4h-9z" fill="#8d8d8d"/><circle cx="5" cy="16" r="2.6" fill="#8d8d8d" stroke="#f3f3f3"/><circle cx="19" cy="16" r="2.6" fill="#8d8d8d" stroke="#f3f3f3"/></svg><span>Versand<br><b>innerhalb 24h</b></span></div>
  <div class="usp-cell"><svg width="25" height="20" viewBox="0 0 25 20"><rect x=".5" y=".5" width="24" height="19" rx="1" fill="#fff" stroke="#999"/><path d="M4 6h2M8 6h13M4 10h2M8 10h13M4 14h2M8 14h13" stroke="#999" stroke-width="1.5"/></svg><span>Über 10.000<br><b>Artikel</b></span></div>
  <div class="usp-cell"><svg width="25" height="25" viewBox="0 0 25 25"><circle cx="12.5" cy="12.5" r="12" fill="#9a9a9a"/><path d="M6 13 12.5 7 19 13M8.5 11v7h8v-7" fill="none" stroke="#fff" stroke-width="2"/></svg><span>Lieferung aus<br><b>der Schweiz</b></span></div>
</aside>

<!-- description -->
<h2 class="abs desc-h">Produktbeschreibung</h2>
<p class="abs desc">Valnorin Schwarzkümmelöl Diese veganen Kapseln von Valnorin enthalten reines und schonend gewonnenes Öl aus ägyptischen Schwarzkümmelsamen sowie Vitamin E. Jede Kapsel enthält 500 mg des wertvollen und kaltgepressten Öls. Die weichen Kapseln sind besonders einfach zu Schlucken, vegan und ohne Konservierungsmittel. Hinweis: Die angegebene empfohlene tägliche Verzehrmenge darf nicht überschritten werden. Nahrungsergänzungsmittel sind kein Ersatz für eine ausgewogene und abwechslungsreiche Ernährung. Für Kinder unzugänglich aufbewahren. (26,65 €/100g) Nahrungsergänzung, Fettsäuren. Das Beste aus dem ägyptischen Schwarzkümmel Vegane Kapseln mit wertvollem Öl aus den Samen von Nigella sativa Aus reinem, kaltgepressten Öl Mit zusätzlichem Vitamin E, welches dazu beiträgt, die Zellen vor oxidativem Stress zu schützen Unter strengen Qualitätskontrollen in der Schweiz hergestellt Ohne Zusatz von Konservierungsmitteln Frei von Lactose und Gluten</p>
<div class="abs rule" style="left:200px;top:585px;width:516px"></div>

<!-- similar -->
<h2 class="abs sim-h">Ähnliche Artikel</h2>
<p class="abs sim-sub">Dolor sit amet</p>
<div class="abs card" style="left:205px"><div class="pic" role="img" aria-label="Produktfoto: Bio-Fruchtsaft mit Schachtel" style="background:linear-gradient(90deg,#7cab4a,#c44 45%,#2a0f14 65%,#5b1020)"></div><div class="p">45.90</div><div class="name">VITARUNA Boost<br>Brausetabl 15 Stk</div></div>
<div class="abs card" style="left:381px"><div class="pic" role="img" aria-label="Produktfoto: Shampoo-Flasche Aloe Vera mit grünem Deckel" style="background:linear-gradient(180deg,#1d5a3a 0%,#1d5a3a 22%,#eef0ec 24%,#e4e8df 100%)"></div><div class="p">5.90</div><div class="name">Super Bio Frucht-<br>Shampoo</div></div>
<div class="abs card" style="left:563px"><div class="pic" role="img" aria-label="Produktfoto: Bio-Fruchtsaft mit Schachtel" style="background:linear-gradient(90deg,#7cab4a,#c44 45%,#2a0f14 65%,#5b1020)"></div><div class="p">8.10</div><div class="name">Super Bio Frucht</div></div>

<!-- service -->
<div class="abs rule" style="left:204px;top:875px;width:653px"></div>
<h3 class="abs q-h">Sie haben Fragen?</h3>
<div class="abs contact" style="left:203px"><svg width="25" height="19" viewBox="0 0 25 19"><rect x="1.2" y="1.2" width="22.6" height="16.6" rx="2" fill="none" stroke="var(--red)" stroke-width="2.2"/><path d="M1.5 2 12.5 11 23.5 2" fill="none" stroke="var(--red)" stroke-width="2.2"/></svg><div><b>E-Mail an</b><span>info@pflegolix.de</span></div></div>
<div class="abs vsep" style="left:421px"></div>
<div class="abs contact" style="left:437px"><svg width="21" height="21" viewBox="0 0 21 21"><path d="M4 1 8 5 6 8c1.5 3 4 5.5 7 7l3-2 4 4-3 3C9 19 2 12 1 4z" fill="var(--red)"/></svg><div><b>Rufen Sie uns an</b><span>Tel.: 01234 567890</span></div></div>
<div class="abs vsep" style="left:650px"></div>
<div class="abs contact" style="left:665px"><svg width="25" height="22" viewBox="0 0 25 22"><ellipse cx="12.5" cy="9.5" rx="11" ry="8" fill="none" stroke="var(--red)" stroke-width="2"/><path d="M6 16 4 21 10 17" fill="none" stroke="var(--red)" stroke-width="2"/></svg><div><b>Kontaktformular</b><span>Hier geht es zum Formular</span></div></div>

<div class="abs rule" style="left:204px;top:973px;width:653px"></div>
<h3 class="abs pay-h">Bezahlmöglichkeiten</h3>
<h3 class="abs ship-h">Versand</h3>
<div class="abs pay" style="left:206px">Veltra</div>
<div class="abs pay-sep" style="left:284px"></div>
<div class="abs pay" style="left:286px">Cardora</div>
<div class="abs pay-sep" style="left:364px"></div>
<div class="abs pay" style="left:366px">PayNest</div>
<div class="abs pay-sep" style="left:446px"></div>
<div class="abs pay" style="left:447px">Zahlwerk Card</div>
<div class="abs pay-sep" style="left:526px"></div>
<div class="abs pay" style="left:527px">Zahlwerk E-Pay</div>
<div class="abs pay-sep" style="left:606px"></div>
<div class="abs pay" style="left:607px">Vorauskasse</div>
<div class="abs pay-sep" style="left:686px"></div>
<div class="abs pay" style="left:688px">Rechnung</div>
<div class="abs pay" style="left:781px">Zahlwerk E-Pay</div>

<!-- footer -->
<div class="abs rule" style="left:204px;top:1065px;width:655px"></div>
<div class="abs f-brand"><i></i><span>pflegolix.ch</span></div>
<p class="abs f-txt" style="left:206px;top:1137px">Lorem ipsum dolor sit amet...</p>
<h4 class="abs f-h" style="left:375px">pflegolix.ch</h4>
<p class="abs f-txt" style="left:375px;top:1117px">Sanaro Handels AG<br>Talackerweg 14<br>8712 Stäfa</p>
<p class="abs f-txt" style="left:375px;top:1160px">Tel.: +41 44 310 27 90<br>E-Mail: info@sanaro-handel.ch</p>
<h4 class="abs f-h" style="left:545px">Service</h4>
<ul class="abs f-list" style="left:547px;top:1117px"><li>AGB</li><li>Impressum</li><li>Versand</li><li>Lorem ipsum</li></ul>
<h4 class="abs f-h" style="left:713px">Newsletter</h4>
<p class="abs f-txt" style="left:712px;top:1117px">Interessante Informationen zum<br>Thema Gesundheit per E-Mail erhalten.</p>
<div class="abs news"><span>Ihre E-Mail Adresse</span><i><svg width="6" height="9" viewBox="0 0 6 9"><path d="M1 1l3.5 3.5L1 8" fill="none" stroke="#fff" stroke-width="1.6"/></svg></i></div>

</body>
</html>
```